Design a Consultation and HR Services Website "Bright Paths"

Consultation and HR Services
I am looking for a design gives the look and feel of Varden Holt and Quillmere
we need a high-quality graphics website that looks rich and expensive.
we are working as an affiliate for international consultation firms and sole agent for international HR products.
we are a group of consultants for the Middle East.
we will get the global practices to local practices.
Updates

Project Deadline Extended
Reason: I am not getting enough options and designs. I am not getting what I was looking for in matter of look and feel. looking for something rich and luxury with black background and rich font. www.gridmarlow.com www.benitavoss.com 17kendalrow.com/ www.trulo.cc/rd/en/ pemberfold.com/ www.trulo.cc/rd/en/ www.zolmi.com/ www.thegildings.co.uk/ .

Target Market(s)

Corporate all size and industries in GCC

Industry/Entity Type

Management Consulting

Coding

Coded - Design and coding required

Number of Pages Required

5+ page

Font styles to use
Sans Serif
Script

Colors
ffffff
ecf7fb
cee9f5
85cae6
33a6d7
0592cd
000000
848484

Requirements
Must have
• This is the looks and feel that I'm looking for.
• http://www.gridmarlow.com/?channel=display&subchannel=pagemuse
• http://www.benitavoss.com/bvny-private/en/
• http://17kendalrow.com/
• http://www.trulo.cc/rd/en/
• http://pemberfold.com/
• http://www.zolmi.com/
• http://www.thegildings.co.uk/
• Home
• Who we are?
• What we do?
• HR & OD Consultation
• Executive Coaching
• Assesment Cemter
• HRIS & Outsourcing
• Testimonials
• Our Partners
• Contact Us
• We need support on Technical righting...

```html
<!DOCTYPE html>
<html lang="en">
<head>
<meta charset="utf-8">
<title>Bright Paths — Consultation &amp; HR Services</title>
<link rel="stylesheet" href="https://fonts.googleapis.com/css2?family=Rajdhani:wght@500;600&family=Lato:wght@400;700&display=swap">
<style>
:root{
  --blue:#22a2cc;
  --blue-deep:#0592cd;
  --blue-light:#33a6d7;
  --ink:#1b1b1b;
  --black:#000;
  --grey:#848484;
  --text:#333;
  --line:#d5d5d5;
  --white:#fff;
  --footer:#3a3a3a;
}
*{box-sizing:border-box;margin:0;padding:0}
html,body{width:1131px;height:1200px;overflow:hidden}
body{position:relative;background:linear-gradient(#f1f1f1,#fff 820px);font-family:"Lato",sans-serif;color:var(--text)}
.abs{position:absolute}
.heading{font-family:"Rajdhani",sans-serif}

.topbar{left:0;top:0;width:1131px;height:34px;background:linear-gradient(90deg,#9a9a9a,#b9b9b9)}
.topbar .left{left:0;top:0;width:566px;height:34px;background:linear-gradient(90deg,#2c9ccd,#40b0da)}
.topbar .item{top:9px;color:#fff;font-family:"Rajdhani",sans-serif;font-weight:600;font-size:14px;display:flex;align-items:center;gap:8px}

.header{left:0;top:34px;width:1131px;height:102px;background:linear-gradient(#f5f5f5,#e9e9e9)}
.brand{left:438px;top:34px;width:256px;height:102px;display:flex;align-items:center;justify-content:center;flex-direction:column;gap:6px}
.brand .name{font-family:"Rajdhani",sans-serif;font-weight:600;font-size:31px;color:var(--blue)}
.brand .mark{width:16px;height:16px;background:var(--blue)}
.nav a{position:absolute;top:87px;font-family:"Rajdhani",sans-serif;font-weight:500;font-size:15px;color:#2a2a2a;text-decoration:none}
.nav a.active{color:var(--blue)}
.nav .underline{left:107px;top:116px;width:45px;height:2px;background:var(--blue)}

.hero{left:0;top:136px;width:1131px;height:418px;background:linear-gradient(100deg,#5b6470 0%,#8f9aa6 35%,#cfd4d9 60%,#9ea6ad 80%,#6a7078 100%)}
.caption{left:102px;top:323px;width:365px;height:77px;background:rgba(60,60,60,.6);color:#fff;font-family:"Rajdhani",sans-serif;font-weight:500;font-size:23px;line-height:30px;padding:7px 14px}
.arrow{top:326px;width:34px;height:34px;background:rgba(40,40,40,.75);display:flex;align-items:center;justify-content:center}

.band{left:0;top:554px;width:1131px;height:144px;background:var(--black)}
.services{left:104px;top:529px;width:923px;height:228px;background:var(--blue);border-radius:5px 5px 0 0;color:#fff}
.services h2{position:absolute;top:16px;width:100%;text-align:center;font-family:"Rajdhani",sans-serif;font-weight:500;font-size:32px}
.services .rule{position:absolute;left:303px;top:66px;width:317px;height:1px;background:#e6f4fa}
.service{position:absolute;top:104px;width:200px;text-align:center}
.service .icon{width:44px;height:44px;margin:0 auto 26px;border-radius:50%;background:#fff;display:flex;align-items:center;justify-content:center}
.service .label{font-family:"Rajdhani",sans-serif;font-weight:500;font-size:19px}

.about{left:105px;top:790px;width:541px;height:251px;background:var(--ink);border-radius:150px 0 0 150px / 125px 0 0 125px;color:#fff}
.about h2{position:absolute;left:76px;top:36px;font-family:"Rajdhani",sans-serif;font-weight:500;font-size:28px}
.about h2 span{color:var(--blue-light)}
.about p{position:absolute;left:76px;top:82px;width:445px;font-size:12.8px;line-height:21.5px}
.about .more{position:absolute;left:78px;top:206px;font-weight:700;font-size:12.5px}

.contact h2{position:absolute;left:684px;top:806px;font-family:"Rajdhani",sans-serif;font-weight:500;font-size:36px;color:#222}
.contact h2 span{color:var(--blue-light)}
.field{position:absolute;left:685px;width:341px;border-bottom:1px solid var(--line);border-right:1px solid var(--line);background:#fff;font-size:12.5px;color:#555;padding:12px 7px}
.submit{left:685px;top:1080px;width:107px;height:37px;background:var(--blue);color:#fff;font-family:"Rajdhani",sans-serif;font-weight:500;font-size:17px;display:flex;align-items:center;justify-content:center}

.info{font-size:11.5px;color:#555;line-height:18px}
.info b{color:#222}
.divider{left:346px;top:1074px;width:1px;height:58px;background:#ccc}

.footer{left:0;top:1158px;width:1131px;height:42px;background:var(--footer)}
.social{top:1166px;width:29px;height:29px;border-radius:50%}
.copy{right:108px;top:1173px;color:#eee;font-size:11px}
</style>
</head>
<body>

<div class="abs topbar">
  <div class="abs left"></div>
  <div class="abs item" style="left:107px">
    <svg width="18" height="16" viewBox="0 0 18 16"><path d="M2 5c0-3 14-3 14 0l-3 1-1-2H6L5 6z" fill="#fff"/><rect x="4" y="7" width="10" height="8" rx="2" fill="#fff"/></svg>
    123-555-0147
  </div>
  <div class="abs item" style="left:842px">
    <svg width="18" height="16" viewBox="0 0 18 16"><path d="M1 7l8-6 8 6v8H1z" fill="none" stroke="#fff" stroke-width="1.6"/><path d="M1 7l8 5 8-5" fill="none" stroke="#fff" stroke-width="1.6"/></svg>
    info@brightpaths.com
  </div>
</div>

<div class="abs header"></div>
<nav class="nav">
  <a class="active" style="left:111px">Home</a>
  <a style="left:191px">Who We Are?</a>
  <a style="left:311px">What We Do?</a>
  <a style="left:738px">Testimonials</a>
  <a style="left:848px">Our Partners</a>
  <a style="left:957px">Contact Us</a>
  <div class="abs underline"></div>
</nav>
<div class="abs brand"><span class="mark"></span><span class="name">Bright Paths</span></div>

<div class="abs hero" role="img" aria-label="Photograph of two business people shaking hands over a meeting table with a tablet"></div>
<div class="abs caption">We Are A Group Of Consultants For The Middle East</div>
<div class="abs arrow" style="left:39px"><svg width="12" height="14"><path d="M10 1L2 7l8 6z" fill="none" stroke="#fff" stroke-width="1.5"/></svg></div>
<div class="abs arrow" style="left:1068px"><svg width="12" height="14"><path d="M2 1l8 6-8 6z" fill="none" stroke="#fff" stroke-width="1.5"/></svg></div>

<div class="abs band"></div>
<section class="abs services">
  <h2>What We Do?</h2>
  <div class="rule"></div>
  <div class="service" style="left:18px"><div class="icon"></div><div class="label">HR &amp; OD Consultation</div></div>
  <div class="service" style="left:259px"><div class="icon"></div><div class="label">Executive Coaching</div></div>
  <div class="service" style="left:500px"><div class="icon"></div><div class="label">Assessment Centre</div></div>
  <div class="service" style="left:741px"><div class="icon"></div><div class="label">HRIS &amp; Outsourcing</div></div>
</section>

<section class="abs about">
  <h2>ABOUT <span>Bright Paths</span></h2>
  <p>Lorem ipsum dolor sit amet, consectetuer adipiscing elit, sed diam nonumm nibh euismod tincidunt ut laoreet dolore magna aliquam erat volutpat. Uteni ad minim veniam, quis nostrud exerci tation ullamcorper suscipit loborti nisl aliquip ex ea commodo consequat. Duis autem vel eum iriure dolor in hendre vulputa nulla facilisis</p>
  <span class="more">Read More »</span>
</section>

<section class="contact">
  <h2><span>QUICK</span> CONTACT</h2>
  <div class="field" style="top:863px;height:36px">Name</div>
  <div class="field" style="top:913px;height:36px">Email</div>
  <div class="field" style="top:963px;height:95px">Message</div>
  <div class="abs submit">Submit</div>
</section>

<div class="abs info" style="left:107px;top:1075px">
  <svg class="abs" style="left:0;top:3px" width="9" height="12"><path d="M4.5 0a4 4 0 0 1 4 4c0 3-4 8-4 8S.5 7 .5 4a4 4 0 0 1 4-4z" fill="#999"/></svg>
  <div style="margin-left:18px"><b>Bright Paths</b><br>123 nonummy nibh &nbsp;tincidun dolore<br>PF magna aliquam e volutpat.</div>
</div>
<div class="abs divider"></div>
<div class="abs info" style="left:383px;top:1082px">
  <div><svg width="10" height="10"><path d="M2 0l2 2-1 2 3 3 2-1 2 2-2 2C4 9 1 6 0 2z" fill="#999"/></svg>&nbsp; <b>123-555-0147</b></div>
  <div style="margin-top:6px"><svg width="10" height="8"><rect width="10" height="8" fill="#999"/></svg>&nbsp; <b>info@brightpaths.com</b></div>
</div>

<footer class="abs footer"></footer>
<div class="abs social" style="left:105px;background:#2a6ab3"></div>
<div class="abs social" style="left:146px;background:#3aa8d8"></div>
<div class="abs social" style="left:188px;background:#d32027"></div>
<div class="abs social" style="left:229px;background:#555"></div>
<div class="abs copy">© 2015 Bright Paths. All Rights Reserved.</div>

</body>
</html>
```